Business Cards/Stationery - Information Technology Company
Dale Porvin Advisory, An Information Technology Services Company
Business Cards/Stationery - Information Technology Company - Information Technology
Creative Brief
Use specific fonts
Whatever works the best.
Simple
Dale Porvin
Solutions Architect & Owner
928 Tarrow Street Suite 504 Glen Ellyn, IL 60139-8812
daleporvin@mailbright.example
http://daleporvin.example
Please use the tagline: "An Information Technology Services Company" under the logo on cards, letterhead, and envelope.
daleporvin daleporvin
Sorry about the long delay. I will be selecting a finalist in the next day.
The NPDX uses the bottom 1/2" of envelopes and prints a black barcode and text when processing. This area should be either be left blank or printed with very light colors or watermark. Designs can have printing on the bottom 1/2" of envelopes as long as it is light enough that NPDX can print its black barcode and it will be visible.
I will rate all designs very soon. Thanks for your patience.
QUIKMAKRR QUIKMAKRR
Star rating please,,,
The two color logo in .ai format has been uploaded and is now available to designers. Sorry about the delay.
The two logo in .ai format has been uploaded and is now available to designers. Sorry about the delay.
I really like the two sided designs that have been submitted so far. I didn't originally plan on a two sided design, but I have changed my mind thanks to all the designer's excellent work. PLEASE SUBMIT ALL FUTURE DESIGNS AS TWO SIDED. Thanks!
ninerock ninerock
Please upload Ai file of your logo!! thnks
I just uploaded the two color version of the logo in .jpg format. I also have .psd and .tif formats available. I don't have an .ai version, but I can get if needed. Please use the two color logo version and let me know if you need anything else. Thanks!

```html
<!DOCTYPE html>
<html lang="en">
<head>
<meta charset="utf-8">
<title>Dale Porvin Advisory — Stationery</title>
<link href="https://fonts.googleapis.com/css2?family=Open+Sans:wght@400;600;700&display=swap" rel="stylesheet">
<style>
  :root {
    --bg: #e3e4e6;
    --paper: #ffffff;
    --navy: #2c3a8e;
    --navy-tint: #e6e9f4;
    --grey: #6d6e72;
    --grey-tint: #d9dadd;
    --ink: #3a3b40;
    --muted: #8a8b90;
  }
  * { margin: 0; padding: 0; box-sizing: border-box; }
  html, body { width: 1200px; height: 961px; overflow: hidden; }
  body {
    background: var(--bg);
    font-family: "Open Sans", sans-serif;
    color: var(--ink);
    position: relative;
  }
  .sheet {
    position: absolute;
    background: var(--paper);
    overflow: hidden;
    box-shadow: 0 6px 18px rgba(0,0,0,0.12);
  }
  .band { position: absolute; left: 0; bottom: 0; width: 100%; display: block; }
  .brand { display: flex; align-items: center; gap: 8px; }
  .brand-square { background: var(--navy); flex: none; }
  .brand-name { color: var(--navy); font-weight: 700; line-height: 1.1; white-space: nowrap; }
  .tagline { color: var(--muted); font-size: 6px; margin-top: 3px; white-space: nowrap; }
  .url {
    position: absolute; color: #fff; font-size: 10px;
    display: flex; align-items: center; gap: 5px;
  }
  .contact { font-size: 7px; line-height: 1.5; color: var(--ink); white-space: nowrap; }
  .contact .row { display: flex; align-items: center; gap: 4px; }

  /* letterhead */
  .letterhead { left: 70px; top: 140px; width: 520px; height: 673px; }
  .letterhead .brand { position: absolute; left: 40px; top: 40px; }
  .letterhead .brand-square { width: 26px; height: 26px; }
  .letterhead .brand-name { font-size: 15px; }
  .letterhead .address { position: absolute; left: 340px; top: 110px; }
  .letterhead .url { left: 40px; bottom: 22px; }

  /* cards */
  .card { top: 140px; width: 250px; height: 143px; }
  .card-front { left: 620px; }
  .card-front .brand { position: absolute; left: 14px; top: 18px; gap: 5px; }
  .card-front .brand-square { width: 14px; height: 14px; }
  .card-front .brand-name { font-size: 9px; }
  .card-front .tagline { font-size: 4.5px; }
  .card-front .person { position: absolute; left: 150px; top: 18px; font-size: 7px; }
  .person .name { font-weight: 700; color: var(--navy); font-size: 8px; }
  .person .title { color: var(--muted); font-size: 5.5px; margin-bottom: 6px; }
  .card-front .contact { font-size: 5.5px; }
  .card-back { left: 890px; background: var(--navy); }
  .card-back .brand { position: absolute; left: 70px; top: 52px; }
  .card-back .brand-square { width: 18px; height: 18px; background: #fff; }
  .card-back .brand-name { color: #fff; font-size: 11px; }
  .card-back .tagline { color: #c9cde6; font-size: 5px; }

  /* envelope: bottom half-inch kept very light for postal barcodes */
  .envelope { left: 620px; top: 587px; width: 520px; height: 226px; }
  .envelope .brand { position: absolute; left: 30px; top: 26px; }
  .envelope .brand-square { width: 22px; height: 22px; }
  .envelope .brand-name { font-size: 13px; }
  .envelope .address { position: absolute; left: 330px; top: 60px; font-size: 7px; line-height: 1.5; }
  .envelope .url { left: 30px; bottom: 32px; font-size: 9px; color: var(--navy); }
</style>
</head>
<body>

<section class="sheet letterhead" aria-label="Letterhead">
  <div class="brand">
    <span class="brand-square"></span>
    <div>
      <div class="brand-name">Dale Porvin Advisory</div>
      <div class="tagline">An Information Technology Services Company</div>
    </div>
  </div>
  <div class="address contact">
    <div>928 Tarrow Street</div>
    <div>Suite 504</div>
    <div>Glen Ellyn, IL 60139-8812</div>
    <div class="row" style="margin-top:6px">
      <svg width="7" height="7" viewBox="0 0 10 10"><path d="M2 1h2l1 2-1.2 1a6 6 0 0 0 2.2 2.2L7 5l2 1v2a1 1 0 0 1-1 1A8 8 0 0 1 1 2a1 1 0 0 1 1-1z" fill="#2c3a8e"/></svg>
      (630) 555-0147
    </div>
    <div class="row">
      <svg width="7" height="7" viewBox="0 0 10 10"><rect x="0.5" y="2" width="9" height="6" fill="none" stroke="#2c3a8e"/><path d="M0.5 2l4.5 3.5L9.5 2" fill="none" stroke="#2c3a8e"/></svg>
      daleporvin@mailbright.example
    </div>
  </div>
  <svg class="band" viewBox="0 0 520 100" height="100" preserveAspectRatio="none">
    <path d="M0 8 C170 40 380 48 520 0 L520 100 L0 100 Z" fill="#6d6e72"/>
    <path d="M0 22 C170 52 380 60 520 14 L520 100 L0 100 Z" fill="#ffffff"/>
    <path d="M0 28 C170 58 380 66 520 20 L520 100 L0 100 Z" fill="#2c3a8e"/>
  </svg>
  <div class="url">
    <svg width="10" height="10" viewBox="0 0 10 10"><circle cx="5" cy="5" r="4.3" fill="none" stroke="#fff"/><ellipse cx="5" cy="5" rx="1.8" ry="4.3" fill="none" stroke="#fff"/><path d="M0.7 5h8.6" stroke="#fff"/></svg>
    http://daleporvin.example
  </div>
</section>

<section class="sheet card card-front" aria-label="Business card front">
  <div class="brand">
    <span class="brand-square"></span>
    <div>
      <div class="brand-name">Dale Porvin Advisory</div>
      <div class="tagline">An Information Technology Services Company</div>
    </div>
  </div>
  <div class="person">
    <div class="name">Dale Porvin</div>
    <div class="title">Solutions Architect &amp; Owner</div>
    <div class="contact">
      <div>928 Tarrow Street Suite 504</div>
      <div>Glen Ellyn, IL 60139-8812</div>
      <div>(630) 555-0147</div>
      <div>daleporvin@mailbright.example</div>
    </div>
  </div>
  <svg class="band" viewBox="0 0 250 40" height="40" preserveAspectRatio="none">
    <path d="M0 4 C90 20 180 22 250 0 L250 40 L0 40 Z" fill="#6d6e72"/>
    <path d="M0 11 C90 25 180 27 250 6 L250 40 L0 40 Z" fill="#ffffff"/>
    <path d="M0 14 C90 28 180 30 250 9 L250 40 L0 40 Z" fill="#2c3a8e"/>
  </svg>
</section>

<section class="sheet card card-back" aria-label="Business card back">
  <svg class="band" viewBox="0 0 250 143" height="143" preserveAspectRatio="none" style="top:0">
    <path d="M0 0 L250 0 L250 10 C170 30 80 28 0 12 Z" fill="#ffffff"/>
    <path d="M0 12 C80 28 170 30 250 10 L250 14 C170 34 80 32 0 16 Z" fill="#6d6e72"/>
  </svg>
  <div class="brand">
    <span class="brand-square"></span>
    <div>
      <div class="brand-name">Dale Porvin Advisory</div>
      <div class="tagline">An Information Technology Services Company</div>
    </div>
  </div>
</section>

<section class="sheet envelope" aria-label="Envelope">
  <div class="brand">
    <span class="brand-square"></span>
    <div>
      <div class="brand-name">Dale Porvin Advisory</div>
      <div class="tagline">An Information Technology Services Company</div>
    </div>
  </div>
  <div class="address">
    <div>928 Tarrow Street</div>
    <div>Suite 504</div>
    <div>Glen Ellyn, IL 60139-8812</div>
  </div>
  <svg class="band" viewBox="0 0 520 70" height="70" preserveAspectRatio="none">
    <path d="M0 6 C170 30 380 34 520 0 L520 70 L0 70 Z" fill="#d9dadd"/>
    <path d="M0 17 C170 40 380 44 520 11 L520 70 L0 70 Z" fill="#ffffff"/>
    <path d="M0 22 C170 45 380 49 520 16 L520 70 L0 70 Z" fill="#e6e9f4"/>
  </svg>
  <div class="url">
    <svg width="9" height="9" viewBox="0 0 10 10"><circle cx="5" cy="5" r="4.3" fill="none" stroke="#2c3a8e"/><ellipse cx="5" cy="5" rx="1.8" ry="4.3" fill="none" stroke="#2c3a8e"/><path d="M0.7 5h8.6" stroke="#2c3a8e"/></svg>
    http://daleporvin.example
  </div>
</section>

</body>
</html>
```